Varbek - Nutritious Snacks and Desserts

We need a creative e-commerce website in which all features--buttons, background, etc.--convey our message: We sell delicious, nutritious snacks and desserts that most closely comply with the paleo diet guidelines. Our first product is Brunavo®--raw, vegan, paleo chocolate balls that are made of dates, coconut, and cocoa. Our products are organic, raw, irresistible and nutritious. We have several versions of Brunavo® in development, as well as mousse, ice cream, and crackers. Our mission is to purvey basic healthy foods. Our motto is, "Fuel for the Daily Trail-Seeker(tm)."

Target Market(s)

Health-conscious professionals who tend to shop at health food stores. Our products also meet the requirements of a gluten-free diet; and they also don't contain refined sugar, so shoppers with gluten and possibly sugar issues are incidental customers.

Industry/Entity Type

Health Product

Coding

Coded - Design and coding required

Number of Pages Required

5+ page

Colors

Designer to choose colors to be used in the design.

Requirements
Must have
• We need at least a home page, a products page, an about-us page, a contact page, and a shopping cart page. We would like to be able to add products on our own later. We should be able to handle some basic coding, especially if it's just a matter of copying and modifying product pages. We would also like the ability in the future to add blogging pages, allowing us to write articles about health food and healthy lifestyle, thus attracting web-traffic (SEO).
• Other features we would like to have:
• Product photo slider on the hopepage
• Back-to-top button at the bottom of the home page
• Make sure the site is mobile-compatible
• A search bar at the top of the homepage
• "Create an account" and "Previous orders"--allowing customers to see their previous orders and reorder what they purchased in the past.
Nice to have
• We would like to convey the paleo theme without actually stating it anywhere. We'll add text as necessary, according to the page layout; you can use ipsum lorem for purpose of demonstration.

```html
<!DOCTYPE html>
<html lang="en">
<head>
<meta charset="utf-8">
<title>Varbek Foods</title>
<link href="https://fonts.googleapis.com/css2?family=Montserrat:wght@400;600;700;800&family=Open+Sans:wght@400;600;700&family=Yellowtail&family=Amatic+SC:wght@700&display=swap" rel="stylesheet">
<style>
:root{
  --green:#5c9c0f;
  --green-light:#7dbd1f;
  --green-dark:#3f6e08;
  --ink:#333;
  --grey:#6d6d6d;
  --paper:#f1f1f1;
  --wood:#2a2824;
  --white:#fff;
}
*{box-sizing:border-box;margin:0;padding:0}
html,body{width:1200px;height:3396px;overflow:hidden}
body{font-family:"Open Sans",sans-serif;color:var(--ink);background:var(--white);position:relative}
.abs{position:absolute}
a{color:inherit;text-decoration:none}

/* top bar */
.topbar{left:0;top:0;width:1200px;height:27px;background:var(--green);color:var(--white);font-size:11px;display:flex;align-items:center;justify-content:space-between;padding:0 120px}
.topbar .links{display:flex;gap:22px}
.topbar span{display:flex;align-items:center;gap:6px}

/* header */
.header{left:0;top:27px;width:1200px;height:138px;background:var(--white);display:flex;align-items:center;padding:0 120px}
.brand{display:flex;align-items:center;gap:12px;font-family:"Montserrat",sans-serif;font-weight:700;font-size:30px;color:var(--green)}
.brand i{width:44px;height:44px;border-radius:50%;background:var(--green-light);display:block}
.nav{display:flex;gap:22px;margin-left:auto;margin-right:60px;font-family:"Montserrat",sans-serif;font-size:15px;color:#444}
.nav li{list-style:none;display:flex;align-items:center;gap:22px}
.nav li+li::before{content:"";width:4px;height:4px;border-radius:50%;background:var(--green)}
.tools{display:flex;gap:24px;align-items:center}

/* hero */
.hero-photo{left:0;top:165px;width:1200px;height:442px;background:radial-gradient(circle at 65% 25%,#c98a3a 0,#8a5a24 22%,#3a3a36 50%,#5a5a58 100%)}
.hero-band{left:0;top:498px;width:1200px;height:109px;background:rgba(20,20,20,.6)}
.hero-title{left:118px;top:518px;font-family:"Montserrat",sans-serif;font-weight:800;font-size:38px;line-height:46px;color:var(--white);white-space:nowrap}
.hero-title em{font-style:normal;color:var(--green-light)}
.hero-sub{left:118px;top:568px;font-size:15px;color:#eee}
.btn{display:inline-flex;align-items:center;gap:10px;background:var(--green-light);color:var(--white);font-family:"Montserrat",sans-serif;font-weight:600;font-size:11px;letter-spacing:.5px;padding:0 18px;height:32px}
.hero-btn{left:958px;top:534px}
.dots{left:1145px;top:348px;display:flex;flex-direction:column;gap:8px}
.dots b{width:8px;height:8px;border-radius:50%;border:1px solid #ccc}
.dots b:first-child{background:var(--green-light);border-color:var(--green-light)}

/* section titles */
.title{width:1200px;left:0;text-align:center}
.title .script{display:block;font-family:"Yellowtail",cursive;font-size:36px;color:var(--green-light);line-height:1}
.title h2{font-family:"Montserrat",sans-serif;font-weight:700;font-size:40px;color:#666;letter-spacing:1px;line-height:1.1}
.title .rule{display:block;width:60px;height:3px;background:var(--green-light);margin:14px auto 0}

/* products */
.products{left:0;top:607px;width:1200px;height:683px;background:var(--paper)}
.product-photo{left:206px;top:790px;width:421px;height:414px;background:linear-gradient(160deg,#7a7a78,#c9c3b6 45%,#8d6a3c 80%,#5b5b58)}
.deal{left:604px;top:810px;width:437px;height:372px;background:var(--white);box-shadow:0 6px 20px rgba(0,0,0,.12);text-align:center;padding-top:22px}
.deal .script{font-family:"Yellowtail",cursive;font-size:34px;color:var(--green-light);line-height:1}
.deal h3{font-family:"Montserrat",sans-serif;font-size:34px;font-weight:700;color:#666;line-height:1}
.deal h4{margin-top:34px;font-family:"Montserrat",sans-serif;font-size:18px;font-weight:700;color:#333;letter-spacing:1px}
.stars{color:var(--green-light);font-size:18px;letter-spacing:2px;margin-top:4px}
.price{font-family:"Montserrat",sans-serif;font-weight:700;color:var(--green-light);font-size:20px}
.deal p{font-size:11px;line-height:1.4;color:var(--grey);width:320px;margin:16px auto 0}
.deal .btn{margin-top:20px;height:36px}
.arrow{top:949px;width:58px;height:58px;background:#c9c9c9;display:flex;align-items:center;justify-content:center}
.arrow.left{left:0}.arrow.right{left:1142px}
.skyline{left:0;top:1212px;width:1200px;height:78px;background:linear-gradient(to bottom,rgba(92,156,15,0) 0,var(--green) 100%)}

/* about */
.about-band{left:0;top:1290px;width:1200px;height:263px;background:var(--green)}
.about-title .script{color:#cfe9a6}
.about-title h2{color:var(--white)}
.about-card{left:97px;top:1431px;width:1006px;height:482px;background:var(--white);box-shadow:0 10px 30px rgba(0,0,0,.12)}
.about-card h3{left:90px;top:52px;width:380px;font-family:"Amatic SC",cursive;font-size:42px;line-height:1.1;color:var(--green);text-transform:uppercase}
.about-card p{left:90px;top:186px;width:420px;font-size:12.5px;line-height:1.65;color:#555;text-align:justify}
.about-card .btn{left:90px;top:380px;height:40px;padding:0 22px}
.about-photo{left:560px;top:50px;width:350px;height:350px;border-radius:50%;background:radial-gradient(circle at 50% 48%,#f6e2b8 0,#d59a4e 28%,#5a3b20 55%,#1b1b1b 72%)}
.badge{left:845px;top:320px;width:96px;height:96px;border-radius:50%;background:var(--white);box-shadow:0 4px 12px rgba(0,0,0,.15);display:flex;align-items:center;justify-content:center;font-family:"Montserrat",sans-serif;font-weight:700;font-size:16px;color:var(--green)}

/* blog */
.post{top:2074px;width:301px;height:453px;border:1px solid #ddd;background:var(--white)}
.post .date{text-align:right;padding:12px 16px 0;font-size:10px;letter-spacing:.5px;color:#555}
.post .thumb{margin-top:10px;height:150px;background:linear-gradient(150deg,#6c5a44,#d4b07c 40%,#2e4f1c 70%,#4a4a46)}
.post h4{padding:32px 18px 0;font-family:"Montserrat",sans-serif;font-size:11.5px;font-weight:700;color:var(--green);letter-spacing:1px}
.post .cat{padding:4px 18px 0;font-size:9.5px;color:#888}
.post p{padding:20px 18px 0;font-size:11.5px;line-height:1.6;color:#666}
.post .foot{position:absolute;left:18px;right:18px;bottom:22px;display:flex;justify-content:space-between;align-items:center}
.outline-btn{border:1px solid var(--green-light);color:var(--green-light);font-size:9.5px;letter-spacing:.5px;padding:9px 14px}
.socials{display:flex;gap:4px}
.socials b{width:18px;height:18px;border-radius:50%;background:var(--green-light)}
.pager{left:528px;top:2566px;display:flex;gap:16px}
.pager b{width:40px;height:3px;background:#ccc}

/* contact */
.call{left:0;top:2610px;width:600px;height:462px;background:var(--green);color:var(--white);text-align:center}
.call .lead{position:absolute;top:160px;width:600px;font-size:14px}
.call .number{position:absolute;left:170px;top:210px;width:260px;height:88px;border:3px solid var(--white);display:flex;align-items:center;justify-content:center;font-family:"Montserrat",sans-serif;font-size:34px;font-weight:600}
.call address{position:absolute;top:370px;width:600px;font-style:normal;font-size:13px;line-height:1.4}
.shout{left:600px;top:2610px;width:600px;height:462px;background:linear-gradient(135deg,#3f5a22,#2b2b29 60%,#4a4a46)}
.shout .kicker{position:absolute;top:50px;width:600px;text-align:center;font-size:9px;letter-spacing:4px;color:#ddd}
.shout h3{position:absolute;top:66px;width:600px;text-align:center;font-family:"Montserrat",sans-serif;font-size:26px;font-weight:700;color:var(--green-light);letter-spacing:1px}
.field{position:absolute;left:37px;width:394px;background:rgba(255,255,255,.8);font-size:11px;color:#555;padding:10px 8px}
.shout .submit{position:absolute;left:37px;top:302px;width:394px;height:36px;background:var(--green-light);color:var(--white);display:flex;align-items:center;justify-content:center;gap:10px;font-family:"Montserrat",sans-serif;font-weight:600;font-size:12px}

/* footer */
.footer{left:0;top:3072px;width:1200px;height:279px;background:linear-gradient(180deg,#34312b,var(--wood) 80%,#2f5710 100%);color:#ddd}
.footer h5{font-family:"Montserrat",sans-serif;font-size:17px;font-weight:700;color:var(--green-light);margin-bottom:14px}
.fcol{position:absolute;top:30px;font-size:11px;line-height:1.55}
.fcol ul{list-style:none}
.fcol li{display:flex;align-items:center;gap:8px;margin-bottom:6px;font-size:12px}
.fcol li i{width:14px;height:14px;border-radius:50%;background:var(--green-light);display:block}
.fcol li i.big{width:22px;height:22px}
.account{display:flex;gap:10px;font-size:13px;align-items:center;color:var(--white)}
.bag{margin-top:26px;display:flex;gap:10px;align-items:center;font-size:15px;color:var(--white)}
.email{margin-top:20px;width:198px;height:26px;background:var(--white);color:#999;font-size:9px;padding:7px}
.subscribe{margin-top:10px;width:108px;height:24px;background:var(--green-light);color:var(--white);font-size:9px;font-weight:700;display:flex;align-items:center;justify-content:center;gap:6px}
.copyright{left:0;top:3351px;width:1200px;height:45px;background:var(--green);color:var(--white);font-size:11px;text-align:center;line-height:45px}
</style>
</head>
<body>

<div class="abs topbar">
  <span><svg width="11" height="11" viewBox="0 0 24 24"><path fill="#fff" d="M6.6 10.8a15 15 0 0 0 6.6 6.6l2.2-2.2c.3-.3.7-.4 1-.2 1.1.4 2.3.6 3.6.6.6 0 1 .4 1 1V20c0 .6-.4 1-1 1A17 17 0 0 1 3 4c0-.6.4-1 1-1h3.5c.6 0 1 .4 1 1 0 1.3.2 2.5.6 3.6.1.3 0 .7-.2 1z"/></svg>(555) 318-2046</span>
  <div class="links"><span>&#9679; Login / Sign up</span><span>&#9829; Wishlist (0)</span><span>&#9711; Checkout</span></div>
</div>

<header class="abs header">
  <div class="brand"><i></i>Varbek</div>
  <ul class="nav"><li>HOME</li><li>ABOUT US</li><li>PRODUCTS</li><li>BLOG</li><li>CONTACT US</li></ul>
  <div class="tools">
    <svg width="22" height="22" viewBox="0 0 24 24"><circle cx="10" cy="10" r="7" fill="none" stroke="#555" stroke-width="2"/><path d="M15 15l6 6" stroke="#555" stroke-width="2"/></svg>
    <svg width="26" height="24" viewBox="0 0 26 24"><path d="M3 8h16l-1.5 14h-13z" fill="none" stroke="#555" stroke-width="2"/><path d="M7 8V5a4 4 0 0 1 8 0v3" fill="none" stroke="#555" stroke-width="2"/><circle cx="21" cy="5" r="5" fill="#5c9c0f"/><text x="21" y="8" font-size="7" fill="#fff" text-anchor="middle" font-family="Open Sans,sans-serif">0</text></svg>
  </div>
</header>

<section>
  <div class="abs hero-photo" role="img" aria-label="Bowl of spiced curry soup topped with red onion and herbs on a dark wooden table"></div>
  <div class="abs hero-band"></div>
  <h1 class="abs hero-title">WELCOME TO <em>VARBEK FOODS.</em></h1>
  <p class="abs hero-sub">Fuel for the Daily Trail-Seeker&trade;</p>
  <a class="abs btn hero-btn">GET STARTED <svg width="14" height="8" viewBox="0 0 14 8"><path d="M0 4h12M9 1l3 3-3 3" stroke="#fff" fill="none" stroke-width="1.4"/></svg></a>
  <div class="abs dots"><b></b><b></b><b></b><b></b></div>
</section>

<section>
  <div class="abs products"></div>
  <div class="abs title" style="top:640px"><span class="script">My Popular</span><h2>PRODUCTS</h2><span class="rule"></span></div>
  <div class="abs product-photo" role="img" aria-label="Paper tub of Brunavo chocolate treats labelled natural, gluten free and vegan raw"></div>
  <div class="abs deal">
    <div class="script">Daily</div>
    <h3>DEALS</h3>
    <h4>BRUNAVO&reg;</h4>
    <div class="stars">&#9733;&#9733;&#9733;&#9733;&#9733;</div>
    <div class="price">$80.00</div>
    <p>Our products are raw, organic, vegan, gluten-free, dairy-free, fiber-rich, nutrient-dense, antioxidant-rich real foods with no preservatives, no added sugar, and no artificial or plant-based sweeteners. And they are irresistibly scrumptious!</p>
    <a class="btn">ADD TO CART <svg width="14" height="14" viewBox="0 0 14 14"><path d="M2 5h10l-1 8H3z M5 5V3a2 2 0 0 1 4 0v2" stroke="#fff" fill="none" stroke-width="1.2"/></svg></a>
  </div>
  <div class="abs arrow left"><svg width="18" height="30" viewBox="0 0 18 30"><path d="M15 2L3 15l12 13" stroke="#fff" fill="none" stroke-width="2"/></svg></div>
  <div class="abs arrow right"><svg width="18" height="30" viewBox="0 0 18 30"><path d="M3 2l12 13L3 28" stroke="#fff" fill="none" stroke-width="2"/></svg></div>
  <div class="abs skyline" role="img" aria-label="Green silhouette of trees and wind turbines along the horizon"></div>
</section>

<section>
  <div class="abs about-band"></div>
  <div class="abs title about-title" style="top:1310px"><span class="script">About</span><h2>VARBEK FOOD</h2></div>
  <svg class="abs" style="left:580px;top:1414px" width="40" height="18" viewBox="0 0 40 18"><path d="M0 18L20 0l20 18z" fill="#fff"/></svg>
  <div class="abs about-card">
    <h3 class="abs">Fuel for<br>the Daily Trail-Seeker&trade;</h3>
    <p class="abs">Lorem Ipsum is simply dummy text of the printing and typesetting industry. Lorem Ipsum has been the industry's standard dummy text ever since the 1500s, when an unknown printer took a galley of type and scrambled it to make a type specimen book. It has survived not only five centuries, but also the leap into electronic typesetting, remaining essentially unchanged. It was popularised in the 1960s with the release of Letraset sheets containing Lorem Ipsum passages.</p>
    <a class="abs btn">READ MORE <svg width="14" height="8" viewBox="0 0 14 8"><path d="M0 4h12M9 1l3 3-3 3" stroke="#fff" fill="none" stroke-width="1.4"/></svg></a>
    <div class="abs about-photo" role="img" aria-label="Stack of pancakes topped with cream and blueberries on a dark plate"></div>
    <div class="abs badge">Varbek</div>
  </div>
</section>

<section>
  <div class="abs title" style="top:1935px"><span class="script">Latest from</span><h2>THE BLOG</h2><span class="rule"></span></div>
  <article class="abs post" style="left:118px">
    <div class="date">MAY 10, 2018, WEDNESDAY</div>
    <div class="thumb" role="img" aria-label="Plate of salad with flatbread"></div>
    <h4>LOREM IPSUM DOLOR SIT AMET</h4><div class="cat">FOOD / PORTFOLIO</div>
    <p>Lorem ipsum dolor sit amet, consectetur adipiscing elit. Sed euismod in tellus in mattis. Aliquam erat volutpat. Praesent ultricies aliquet erat a semper.</p>
    <div class="foot"><span class="outline-btn">READ MORE</span><span class="socials"><b></b><b></b><b></b><b></b></span></div>
  </article>
  <article class="abs post" style="left:448px">
    <div class="date">MAY 10, 2018, WEDNESDAY</div>
    <div class="thumb" role="img" aria-label="Plate of salad with flatbread"></div>
    <h4>LOREM IPSUM DOLOR SIT AMET</h4><div class="cat">FOOD / PORTFOLIO</div>
    <p>Lorem ipsum dolor sit amet, consectetur adipiscing elit. Sed euismod in tellus in mattis. Aliquam erat volutpat. Praesent ultricies aliquet erat a semper.</p>
    <div class="foot"><span class="outline-btn">READ MORE</span><span class="socials"><b></b><b></b><b></b><b></b></span></div>
  </article>
  <article class="abs post" style="left:779px">
    <div class="date">MAY 10, 2018, WEDNESDAY</div>
    <div class="thumb" role="img" aria-label="Plate of salad with flatbread"></div>
    <h4>LOREM IPSUM DOLOR SIT AMET</h4><div class="cat">FOOD / PORTFOLIO</div>
    <p>Lorem ipsum dolor sit amet, consectetur adipiscing elit. Sed euismod in tellus in mattis. Aliquam erat volutpat. Praesent ultricies aliquet erat a semper.</p>
    <div class="foot"><span class="outline-btn">READ MORE</span><span class="socials"><b></b><b></b><b></b><b></b></span></div>
  </article>
  <div class="abs pager"><b></b><b></b><b></b></div>
</section>

<section>
  <div class="abs call">
    <svg style="position:absolute;left:272px;top:62px" width="56" height="56" viewBox="0 0 24 24"><path fill="#fff" d="M6.6 10.8a15 15 0 0 0 6.6 6.6l2.2-2.2c.3-.3.7-.4 1-.2 1.1.4 2.3.6 3.6.6.6 0 1 .4 1 1V20c0 .6-.4 1-1 1A17 17 0 0 1 3 4c0-.6.4-1 1-1h3.5c.6 0 1 .4 1 1 0 1.3.2 2.5.6 3.6.1.3 0 .7-.2 1z"/></svg>
    <p class="lead">24/7 Assistance. Call us any time.</p>
    <div class="number">(555) 318-204</div>
    <svg style="position:absolute;left:286px;top:334px" width="28" height="28" viewBox="0 0 28 28"><rect x="1" y="1" width="26" height="26" fill="none" stroke="#fff" stroke-width="2"/><path d="M14 6a5 5 0 0 0-5 5c0 4 5 10 5 10s5-6 5-10a5 5 0 0 0-5-5z" fill="#fff"/><circle cx="14" cy="11" r="2" fill="#5c9c0f"/></svg>
    <address>48 ORCHARD LANE<br>FERNVALE, OR 97001</address>
  </div>
  <div class="abs shout" role="img" aria-label="Hands serving a plate of food, darkened behind the contact form">
    <div class="kicker">CONTACT US</div>
    <h3>GIVE US A SHOUT</h3>
    <div class="field" style="top:110px">Enter Name</div>
    <div class="field" style="top:154px">Enter Email</div>
    <div class="field" style="top:198px;height:86px">Enter Message</div>
    <div class="submit">SUBMIT <svg width="14" height="8" viewBox="0 0 14 8"><path d="M0 4h12M9 1l3 3-3 3" stroke="#fff" fill="none" stroke-width="1.4"/></svg></div>
  </div>
</section>

<footer>
  <div class="abs footer">
    <div class="fcol" style="left:122px;width:200px">
      <h5>ABOUT US</h5>
      <div style="color:#fff;font-size:11px;margin-bottom:8px">VARBEK FOODS</div>
      <p>Our products are raw, organic, vegan, gluten-free, dairy-free, fiber-rich, nutrient-dense, antioxidant rich real foods with no preservatives, no added sugar, and no artificial or plant-based sweeteners.</p>
      <p style="margin-top:10px">And they are irresistibly scrumptious!</p>
    </div>
    <div class="fcol" style="left:400px">
      <h5>QUICK LINKS</h5>
      <ul><li><i></i>HOME</li><li><i></i>ABOUT US</li><li><i></i>PRODUCTS</li><li><i></i>BLOG</li><li><i></i>CONTACT US</li></ul>
    </div>
    <div class="fcol" style="left:630px">
      <h5>CONNECT WITH US</h5>
      <ul><li><i class="big"></i>FEEDLINE</li><li><i class="big"></i>CHIRPER</li><li><i class="big"></i>SNAPFRAME</li><li><i class="big"></i>CIRCLENET</li></ul>
    </div>
    <div class="fcol" style="left:884px;top:36px">
      <div class="account"><span>&#10140; LOGIN</span><span>|</span><span>&#9679; REGISTER</span></div>
      <div class="bag"><svg width="20" height="20" viewBox="0 0 20 20"><path d="M2 7h16l-1 12H3z" fill="#7dbd1f"/><path d="M6 7V5a4 4 0 0 1 8 0v2" stroke="#7dbd1f" fill="none" stroke-width="2"/></svg>SHOPPING BAG (0)</div>
      <div class="email">YOUR E-MAIL</div>
      <div class="subscribe">SUBSCRIBE &rarr;</div>
    </div>
  </div>
  <div class="abs copyright">&copy; 2018 Varbek Foods , All Right Reserved.</div>
</footer>

</body>
</html>
```